Landing page for a sports website

we have a sports tracking and management website and require a web site.
the site should have the ability to have 2 options for selection the first being a competitions portal the other a club portal there should be a about us page and a contact us page
the site should be dynamic and vibrant and be easily recognisable as a multiple sports page
we also have www.tilvoshelf.net and would like it to compliment that site
i would like to have some form of animation regarding sports occur when you click the login option if that is possible
the site is www.drqplays.net and I have attached the logo in both 3d and standard
we also require a design several templates for information pages please see www.lunaforge.net as an example of how it should look but with a sports theme
Target Market(s)
This will be used for primarily team based sports
Industry/Entity Type
Management
Number of Pages Required
3 page
Requirements
Must have
- the ability to change the logo and names of the site
- i.e. from drqplays to drqcampus at a later date

```html
<!DOCTYPE html>
<html lang="en">
<head>
<meta charset="utf-8">
<title>DRQ Plays – Sports Tracking and Management</title>
<link href="https://fonts.googleapis.com/css2?family=Oswald:wght@400;500&family=Raleway:wght@400;500;600&family=Roboto:ital,wght@0,400;0,500;1,400&display=swap" rel="stylesheet">
<style>
  :root {
    --header-bg: #2f3a49;
    --stadium-dark: #1a1e25;
    --stadium-mid: #3b3f47;
    --haze: #5c5c61;
    --track: #5a3a33;
    --track-deep: #2c1f1e;
    --skin-warm: #a8735a;
    --kit-dark: #16171b;
    --accent-line: #2d5f8a;
    --features-bg: #121821;
    --testimonials-bg: #2d3644;
    --footer-bg: #111419;
    --orange: #f7923a;
    --orange-light: #ffc23a;
    --blue-btn: #2a7cc4;
    --blue-btn-dark: #0c3d70;
    --login: #1bb0e2;
    --logo-cyan: #36b9e0;
    --white: #ffffff;
    --text-soft: #dfe3e8;
    --quote-mark: #8e97a3;
    --social: #3d4756;
  }
  * { margin: 0; padding: 0; box-sizing: border-box; }
  html, body { width: 918px; height: 1200px; overflow: hidden; background: var(--footer-bg); }
  body { position: relative; font-family: "Roboto", Arial, sans-serif; color: var(--white); }

  .site-header { position: absolute; left: 0; top: 0; width: 918px; height: 110px; background: var(--header-bg); box-shadow: 0 2px 4px rgba(0,0,0,.35); z-index: 2; }
  .brand { position: absolute; left: 68px; top: 36px; display: flex; align-items: center; gap: 8px;
    font-family: "Raleway", sans-serif; font-weight: 600; font-size: 26px; color: var(--logo-cyan); letter-spacing: 1px; }
  .brand-mark { width: 16px; height: 16px; background: var(--orange); border-radius: 50%; }
  .main-nav { position: absolute; left: 386px; top: 49px; display: flex; gap: 24px; font-size: 11px; letter-spacing: .3px; }
  .main-nav a { color: var(--white); text-decoration: none; }
  .login-btn { position: absolute; left: 773px; top: 40px; width: 70px; height: 31px; background: var(--login);
    border-radius: 2px; font-size: 11px; line-height: 31px; text-align: center; }

  .hero { position: absolute; left: 0; top: 110px; width: 918px; height: 472px; overflow: hidden; }
  .hero-photo { position: absolute; inset: 0;
    background:
      linear-gradient(90deg, rgba(18,20,26,.55) 0%, rgba(18,20,26,.15) 45%, rgba(0,0,0,0) 60%),
      radial-gradient(ellipse 70px 200px at 690px 200px, rgba(22,23,27,.9), transparent 75%),
      radial-gradient(ellipse 150px 230px at 680px 230px, rgba(168,115,90,.55), transparent 72%),
      radial-gradient(ellipse 230px 90px at 640px 430px, rgba(150,120,110,.35), transparent 70%),
      radial-gradient(ellipse 520px 200px at 460px 140px, rgba(92,92,97,.55), transparent 70%),
      linear-gradient(180deg, var(--stadium-dark) 0%, var(--stadium-mid) 30%, #3f3b3f 52%, var(--track) 72%, #4a302c 88%, var(--track-deep) 100%); }
  .hero-title { position: absolute; left: 68px; top: 116px; font-family: "Oswald", sans-serif; font-weight: 500; font-size: 54px; line-height: 1; letter-spacing: -.5px; text-shadow: 0 2px 4px rgba(0,0,0,.5); }
  .hero-sub { position: absolute; left: 68px; top: 193px; font-family: "Raleway", sans-serif; font-weight: 500; font-size: 20px; }
  .hero-text { position: absolute; left: 68px; top: 225px; width: 400px; font-family: "Raleway", sans-serif; font-size: 15px; line-height: 21px; }
  .portal-btn { position: absolute; top: 283px; height: 39px; border-radius: 3px; font-family: "Oswald", sans-serif;
    font-size: 15px; line-height: 39px; text-align: center; box-shadow: 0 2px 4px rgba(0,0,0,.45); }
  .portal-competition { left: 70px; width: 156px; background: linear-gradient(180deg, var(--orange-light) 0%, #ffae2e 45%, var(--orange) 55%, #f57a1f 100%); }
  .portal-club { left: 240px; width: 135px; background: linear-gradient(180deg, var(--blue-btn) 0%, #1d63a6 45%, var(--blue-btn-dark) 55%, #1a5596 100%); }
  .hero-rule { position: absolute; left: 0; top: 582px; width: 918px; height: 3px; background: var(--accent-line); }

  .features { position: absolute; left: 0; top: 585px; width: 918px; height: 255px; background: var(--features-bg); }
  .feature { position: absolute; top: 44px; width: 220px; text-align: center; }
  .feature-icon { width: 82px; height: 82px; margin: 0 auto; border-radius: 50%; background: var(--orange);
    border: 3px solid var(--white); display: flex; align-items: center; justify-content: center; }
  .feature h2 { margin-top: 17px; font-family: "Raleway", sans-serif; font-weight: 500; font-size: 14px; }
  .feature p { width: 200px; margin: 12px auto 0; font-size: 9.5px; line-height: 15.5px; color: var(--text-soft); }

  .testimonials { position: absolute; left: 0; top: 840px; width: 918px; height: 253px; background: var(--testimonials-bg); }
  .testimonials h2 { position: absolute; left: 0; top: 46px; width: 918px; text-align: center;
    font-family: "Oswald", sans-serif; font-weight: 400; font-size: 18px; }
  .quote-card { position: absolute; top: 103px; width: 270px; height: 110px; }
  .avatar { position: absolute; left: 0; top: 0; width: 75px; height: 75px; border-radius: 50%; border: 2px solid var(--white);
    background: radial-gradient(circle at 50% 40%, #c9a58c, #7d8c9c); }
  .quote-open, .quote-close { position: absolute; font-family: "Raleway", sans-serif; font-size: 30px; line-height: 1; color: var(--quote-mark); }
  .quote-open { left: 87px; top: 1px; }
  .quote-close { left: 234px; top: 56px; }
  .quote-text { position: absolute; left: 105px; top: 14px; width: 135px; font-style: italic; font-size: 9.5px; line-height: 17px; }
  .quote-name { position: absolute; left: 102px; top: 79px; font-size: 9.5px; font-weight: 500; color: var(--orange); }
  .quote-role { position: absolute; left: 102px; top: 94px; font-size: 9.5px; font-style: italic; }

  .site-footer { position: absolute; left: 0; top: 1093px; width: 918px; height: 107px; background: var(--footer-bg); }
  .footer-links { position: absolute; left: 75px; top: 32px; font-size: 10px; }
  .footer-links span { margin: 0 4px; }
  .copyright { position: absolute; left: 75px; top: 53px; font-size: 12px; }
  .social { position: absolute; left: 725px; top: 36px; display: flex; gap: 7px; }
  .social span { width: 26px; height: 26px; background: var(--social); border-radius: 2px; }
</style>
</head>
<body>
  <header class="site-header">
    <div class="brand"><span class="brand-mark"></span>DRQ PLAYS</div>
    <nav class="main-nav">
      <a href="#">HOME</a><a href="#">ABOUT US</a><a href="#">FEATURES</a><a href="#">NEWS</a><a href="#">BLOG</a><a href="#">CONTACT</a>
    </nav>
    <div class="login-btn">LOGIN</div>
  </header>

  <section class="hero">
    <div class="hero-photo" role="img" aria-label="Sprinter in motion racing along a stadium running track at dusk"></div>
    <h1 class="hero-title">DRQ PLAYS</h1>
    <p class="hero-sub">SPORTS TRACKING AND MANAGEMENT</p>
    <p class="hero-text">Lorem Ipsum has been the industry's standard dummy text ever since the 1500s, when an unknown printer</p>
    <div class="portal-btn portal-competition">COMPETITION PORTAL</div>
    <div class="portal-btn portal-club">CLUB PORTAL</div>
  </section>
  <div class="hero-rule"></div>

  <section class="features">
    <div class="feature" style="left:67px">
      <div class="feature-icon">
        <svg width="26" height="28" viewBox="0 0 26 28"><circle cx="13" cy="8" r="7" fill="#fff"/><rect x="1" y="16" width="24" height="12" rx="5" fill="#fff"/></svg>
      </div>
      <h2>WHAT WE DO</h2>
      <p>Lorem Ipsum has been the industry's standard dummy text ever since the 1500s, when an unknown printer took a galley of type</p>
    </div>
    <div class="feature" style="left:347px">
      <div class="feature-icon">
        <svg width="32" height="32" viewBox="0 0 32 32"><path d="M30 2 L2 14 L12 18 L14 30 L19 21 Z" fill="#fff"/><path d="M30 2 L12 18" stroke="#f7923a" stroke-width="2"/></svg>
      </div>
      <h2>SPORTS TRACKING</h2>
      <p>Lorem Ipsum has been the industry's standard dummy text ever since the 1500s, when an unknown printer took a galley of type</p>
    </div>
    <div class="feature" style="left:626px">
      <div class="feature-icon">
        <svg width="34" height="28" viewBox="0 0 34 28"><circle cx="7" cy="8" r="4.5" fill="#fff"/><circle cx="27" cy="8" r="4.5" fill="#fff"/><circle cx="17" cy="9" r="6" fill="#fff"/><rect x="0" y="14" width="12" height="9" rx="4" fill="#fff"/><rect x="22" y="14" width="12" height="9" rx="4" fill="#fff"/><rect x="8" y="16" width="18" height="12" rx="5" fill="#fff"/></svg>
      </div>
      <h2>MANAGEMENT</h2>
      <p>Lorem Ipsum has been the industry's standard dummy text ever since the 1500s, when an unknown printer took a galley of type</p>
    </div>
  </section>

  <section class="testimonials">
    <h2>3500+ HAPPY USERS IN INDIA, MANY MORE AROUND THE WORLD</h2>
    <div class="quote-card" style="left:67px">
      <div class="avatar" role="img" aria-label="Portrait photo of a smiling user"></div>
      <span class="quote-open">“</span><span class="quote-close">”</span>
      <p class="quote-text">Lorem Ipsum is simply dummy text of the printing and typeset-ting industry.</p>
      <p class="quote-name">LENA MORAVIK</p><p class="quote-role">Marketing Executive</p>
    </div>
    <div class="quote-card" style="left:337px">
      <div class="avatar" role="img" aria-label="Portrait photo of a smiling user"></div>
      <span class="quote-open">“</span><span class="quote-close">”</span>
      <p class="quote-text">Lorem Ipsum is simply dummy text of the printing and typeset-ting industry.</p>
      <p class="quote-name">LENA MORAVIK</p><p class="quote-role">Marketing Executive</p>
    </div>
    <div class="quote-card" style="left:601px">
      <div class="avatar" role="img" aria-label="Portrait photo of a smiling user"></div>
      <span class="quote-open">“</span><span class="quote-close">”</span>
      <p class="quote-text">Lorem Ipsum is simply dummy text of the printing and typeset-ting industry.</p>
      <p class="quote-name">LENA MORAVIK</p><p class="quote-role">Marketing Executive</p>
    </div>
  </section>

  <footer class="site-footer">
    <p class="footer-links">About<span>|</span>Disclaimer<span>|</span>Contact<span>|</span>Sitemap<span>|</span>Special Thanks</p>
    <p class="copyright">Copyright © 2015&nbsp; All Rights</p>
    <div class="social">
      <span aria-label="Social link"></span><span aria-label="Social link"></span><span aria-label="Social link"></span><span aria-label="Social link"></span>
    </div>
  </footer>
</body>
</html>
```